IT Consulting Firm Website
Core Values: Proficiency ♦ Consistency ♦ Integrity
IT Consulting Firm Website - Information Technology
Creative Brief
Information Technology
www.dunmorevantage.com
Premier IT Services Consulting firm with a heavy emphasis on ethical business practices and superior technical skillsets. Dunmore Consulting designs and implements effective solutions that are specific to the client's information technology issues and business model. Harness our ability to assess your information technology concerns and deliver a solution that meets the company's current requirements and plan appropriately for the company's future demands. DCHP understands how technology works and has a clear focus enabling us to accurately read the strategic big picture of any business challenge. Business continuity and disaster recovery plans are also addressed and implemented as part of the IT solution. Dunmore Consulting has led successful efforts in delivering effective IT solutions to difficult and complex business challenges.
we are looking for a website design that will establish our brand as professional, ethical and technically superior to our competitors. Nothing cartoonish. Something that will identify us by the solid and stable IT industry relationships we've developed.
Modern
Core color is Cobalt Blue (Pantone 288C - RGB 00337F)
RGB 1975FF
RGB 3F3F3F & RGB 000000
below header
Please use images from www.lumepixbank.com Also, please make sure you guys use our NEW logo that I've uploaded to the project and to design with that in mind. Not our old logo that you see on the website.

```html
<!DOCTYPE html>
<html lang="en">
<head>
<meta charset="utf-8">
<title>Dunmore Consulting Group</title>
<link rel="stylesheet" href="https://fonts.googleapis.com/css2?family=Arimo:wght@400;700&family=Roboto+Condensed:wght@700&display=swap">
<style>
:root{
  --cobalt:#00337f;
  --bright:#1975ff;
  --sky:#2f7fd8;
  --navy:#0b1f3f;
  --ink:#3f3f3f;
  --black:#000;
  --muted:#777;
  --line:#dcdfe4;
  --paper:#fff;
  --mist:#eef1f5;
}
*{margin:0;padding:0;box-sizing:border-box}
html,body{width:1200px;height:1025px;overflow:hidden}
body{font-family:"Arimo",Arial,sans-serif;color:var(--ink);background:var(--paper);position:relative}
.page{position:relative;width:1200px;height:1025px;background:linear-gradient(#fff 0,#fff 95px,#3a78c4 95px,#6fa3dc 250px,#dfe8f3 470px,#fff 560px,#fff 100%)}
.abs{position:absolute}
/* header */
.brand{left:262px;top:18px;display:flex;align-items:center;gap:12px}
.brand-mark{width:44px;height:44px;border-radius:50%;background:var(--cobalt)}
.brand-name{font-size:40px;font-weight:700;color:var(--cobalt);line-height:1}
.brand-sub{font-size:15px;color:var(--cobalt);margin-top:4px}
.contact{left:800px;top:10px}
.contact-label{position:absolute;left:46px;top:6px;font-size:10px;color:var(--muted)}
.contact-phone{position:absolute;left:46px;top:18px;font-size:25px;color:var(--ink);white-space:nowrap}
.contact-web{position:absolute;left:46px;top:46px;font-size:11px;color:var(--cobalt);white-space:nowrap}
.offices{left:800px;top:68px;width:230px;height:26px;background:var(--bright);color:#fff;font-size:13px;line-height:26px;padding-left:12px;border-radius:3px 3px 0 0}
/* hero */
.hero{left:189px;top:111px;width:825px;height:318px;background:#fff;border-radius:8px;box-shadow:0 4px 14px rgba(0,0,0,.25);overflow:hidden}
.hero-photo{position:absolute;left:286px;top:10px;width:528px;height:258px;border-radius:4px;background:linear-gradient(120deg,#e9eef4,#b8c8da 55%,#5d7593)}
.hero-copy{position:absolute;left:28px;top:94px}
.hero-line{font-size:22px;font-weight:700;color:var(--ink)}
.hero-line b{color:var(--bright)}
.hero-headline{font-family:"Roboto Condensed",Arial,sans-serif;font-size:54px;color:var(--bright);line-height:1.05;margin:6px 0 4px;white-space:nowrap}
.hero-tag{font-size:22px;color:var(--ink)}
.hero-dots{position:absolute;right:30px;top:248px;display:flex;gap:7px}
.hero-dots span{width:10px;height:10px;border-radius:50%;background:#fff;opacity:.8}
.nav{position:absolute;left:0;bottom:0;width:100%;height:38px;background:linear-gradient(var(--navy),#051126);display:flex;padding-left:20px}
.nav a{color:#fff;font-size:14px;text-decoration:none;line-height:38px;padding:0 30px}
.nav a.is-active{background:var(--bright)}
/* welcome */
.welcome{left:200px;top:448px;width:560px}
.welcome-title{display:flex;align-items:center;gap:12px;font-size:30px;color:var(--ink)}
.welcome-title strong{color:var(--black)}
.welcome-dot{width:40px;height:40px;border-radius:50%;background:var(--cobalt)}
.welcome p{font-size:12.5px;line-height:1.5;margin-top:8px;color:var(--ink)}
.promo{left:790px;top:445px;width:225px;height:112px;border-radius:6px;overflow:hidden;background:linear-gradient(135deg,#c9d3de,#6f8aa6)}
.promo-bar{position:absolute;left:0;bottom:0;width:100%;height:28px;background:#2e8b3e;color:#fff;font-size:12px;line-height:28px;text-align:right;padding-right:14px}
/* services */
.services{left:190px;top:580px;width:825px;height:270px;display:flex}
.service{flex:1;position:relative;padding:18px 14px 0;border-right:1px solid var(--line)}
.service:last-child{border-right:0}
.service-photo{height:108px;border-radius:4px;background:linear-gradient(135deg,#eef2f6,#9fb3c8)}
.service h3{font-size:19px;font-weight:400;color:var(--black);margin:14px 0 8px;white-space:nowrap}
.service ul{list-style:none;font-size:12.5px;line-height:1.55;color:var(--ink)}
.service li::before{content:"\203A";color:var(--bright);margin-right:6px;font-weight:700}
.learn{position:absolute;right:14px;bottom:6px;width:96px;height:28px;background:var(--cobalt);color:#fff;font-size:12px;text-align:center;line-height:28px;border-radius:14px 0 0 0}
/* partners */
.partners{left:195px;top:862px;width:815px;height:68px;background:linear-gradient(#fbfbfc,#dfe3e8);border:1px solid #cfd4da;border-radius:8px;display:flex;align-items:center;justify-content:space-around;padding:0 50px}
.partner{width:95px;height:32px;border-radius:4px;background:#c4cad2}
.partner.round{width:40px;height:40px;border-radius:50%}
.arrow{top:878px;width:34px;height:36px}
/* footer */
.footer{left:0;top:945px;width:1200px;height:80px;background:var(--black)}
.footer-brand{position:absolute;left:200px;top:18px;display:flex;align-items:center;gap:8px;color:#ccc;font-size:22px;font-weight:700}
.footer-brand span{width:24px;height:24px;border-radius:50%;background:#777}
.footer-nav{position:absolute;left:355px;top:22px;font-size:13px;color:#ddd;word-spacing:2px}
.footer-copy{position:absolute;left:355px;top:46px;font-size:10px;color:#888}
</style>
</head>
<body>
<div class="page">

  <header>
    <div class="abs brand">
      <div class="brand-mark"></div>
      <div>
        <div class="brand-name">DUNMORE</div>
        <div class="brand-sub">Consulting Group</div>
      </div>
    </div>
    <div class="abs contact">
      <svg width="38" height="34" viewBox="0 0 38 34"><rect x="3" y="10" width="32" height="20" rx="4" fill="#9aa3ad"/><path d="M2 12 Q19 -2 36 12 L30 15 Q19 7 8 15Z" fill="#6c757f"/><rect x="12" y="16" width="14" height="9" rx="2" fill="#e3e6ea"/></svg>
      <span class="contact-label">Quick Contact</span>
      <span class="contact-phone">702.555.0148</span>
      <span class="contact-web">www.dunmorevantage.com</span>
    </div>
    <div class="abs offices">Offices: Las Vegas &amp; Reno</div>
  </header>

  <section class="abs hero">
    <div class="hero-photo" role="img" aria-label="Photo of a business team meeting around a conference table"></div>
    <div class="hero-copy">
      <div class="hero-line">Dunmore Consulting <b>is a</b></div>
      <div class="hero-headline">Nevada-based IT firm</div>
      <div class="hero-tag">that delivers innovative IT solutions</div>
    </div>
    <div class="hero-dots"><span></span><span></span><span></span><span></span></div>
    <nav class="nav">
      <a class="is-active">Home</a><a>About Us</a><a>Company</a><a>Solutions</a><a>Partners &amp; Certifications</a><a>Contact Us</a>
    </nav>
  </section>

  <section class="abs welcome">
    <div class="welcome-title"><span class="welcome-dot"></span><span>Welcome to <strong>DUNMORE</strong></span></div>
    <p>Dunmore Consulting Group understands what small businesses require since our inception in 2005. We possess the experience, certifications, and ability to provide industry best practices in information technology solutions.</p>
  </section>
  <div class="abs promo" role="img" aria-label="Photo of a business professional at work">
    <div class="promo-bar">click for more details ›</div>
  </div>

  <section class="abs services">
    <article class="service">
      <div class="service-photo" role="img" aria-label="Photo of a technician working at a computer"></div>
      <h3>Network Integration</h3>
      <ul><li>Infrastructure Analysis</li><li>Improved Scalability</li><li>Business Continuity</li></ul>
      <span class="learn">Learn More</span>
    </article>
    <article class="service">
      <div class="service-photo" role="img" aria-label="Photo of a support agent with a headset"></div>
      <h3>Managed I.T. Services</h3>
      <ul><li>Network Performance</li><li>Data Storage &amp; Management</li><li>Security Monitoring</li></ul>
      <span class="learn">Learn More</span>
    </article>
    <article class="service">
      <div class="service-photo" role="img" aria-label="Photo of server and cloud computing equipment"></div>
      <h3>Virtualization &amp; Cloud Computing</h3>
      <ul><li>Simplify Management</li><li>Optimized Operational Efficiency</li><li>IT Services On Demand</li></ul>
      <span class="learn">Learn More</span>
    </article>
  </section>

  <section class="abs partners" aria-label="Technology partners">
    <div class="partner"></div>
    <div class="partner round"></div>
    <div class="partner"></div>
    <div class="partner round"></div>
    <div class="partner"></div>
    <div class="partner"></div>
  </section>
  <svg class="abs arrow" style="left:200px" viewBox="0 0 34 36"><path d="M22 8 L10 18 L22 28" fill="none" stroke="#6c7784" stroke-width="4"/></svg>
  <svg class="abs arrow" style="left:970px" viewBox="0 0 34 36"><path d="M12 8 L24 18 L12 28" fill="none" stroke="#6c7784" stroke-width="4"/></svg>

  <footer class="abs footer">
    <div class="footer-brand"><span></span>DUNMORE</div>
    <div class="footer-nav">Home &nbsp;|&nbsp; About Us &nbsp;|&nbsp; Company &nbsp;|&nbsp; Solutions &nbsp;|&nbsp; Partners &amp; Certifications &nbsp;|&nbsp; Contact Us</div>
    <div class="footer-copy">Copyright 2010 Dunmore Consulting Group. All Rights Reserved.</div>
  </footer>

</div>
</body>
</html>
```